7Bram Plumbing flyer

I want to incorporate our logo design into a new flyer promoting the business and advertising products that we install.
We install hot water systems, Air-conditioning systems and central heating systems. Along with other aspects of plumbing such as gasfitting, roofing, sanitary and drainage
I would like the background to be the same as our business cards with the water effect and colours.

Requirements
Must have
• Logo
24/7 Emergency call out
Aspects of plumbing we do
- Hot water systems
- Central Heating
- Solar hot water systems/ heat pump systems
- Gasfitting
- Drainage
- Roofing
- Air-Conditioning
Nice to have
• Pictures of hot water systems and air-conditioning system
$30 off voucher when producing this flyer (limit 1 per house hold)

```html
<!DOCTYPE html>
<html lang="en">
<head>
<meta charset="utf-8">
<title>7Bram Plumbing Flyer</title>
<link rel="stylesheet" href="https://fonts.googleapis.com/css2?family=Montserrat:wght@500;600;700;800;900&family=Oswald:wght@500;600&display=swap">
<style>
  :root {
    --page: #f1f1f1;
    --charcoal: #3b3c3e;
    --charcoal-dark: #2c2d2f;
    --brand-blue: #1478c8;
    --bright-blue: #1aa3e8;
    --deep-blue: #0d5ea6;
    --alert-red: #c21d3a;
    --white: #ffffff;
    --soft-white: #e9eef3;
    --ring-grey: #d5dde6;
    --body-font: "Montserrat", Arial, sans-serif;
    --display-font: "Oswald", "Arial Narrow", sans-serif;
  }
  * { box-sizing: border-box; margin: 0; padding: 0; }
  html, body { width: 777px; height: 1200px; overflow: hidden; }
  body { background: var(--page); font-family: var(--body-font); position: relative; }

  .flyer {
    position: absolute; left: 193px; width: 390px; height: 554px; overflow: hidden;
    background: radial-gradient(ellipse at 40% 30%, #48494c 0%, var(--charcoal) 55%, var(--charcoal-dark) 100%);
    box-shadow: 0 4px 14px rgba(0,0,0,.28);
  }
  .flyer--front { top: 31px; }
  .flyer--back { top: 615px; }
  .flyer__shapes { position: absolute; inset: 0; }

  /* brand lockup */
  .brand { position: absolute; left: 30px; top: 34px; display: flex; align-items: center; gap: 8px; }
  .brand__dot { width: 40px; height: 40px; border-radius: 50%; background: var(--brand-blue); }
  .brand__name { color: var(--bright-blue); font-weight: 800; font-size: 17px; line-height: 1; letter-spacing: .5px; text-transform: uppercase; }

  .headline { position: absolute; left: 28px; top: 104px; text-transform: uppercase; line-height: 1; }
  .headline__name { display: block; color: var(--bright-blue); font-weight: 900; font-size: 41px; letter-spacing: .5px; }
  .headline__trade { display: block; color: var(--white); font-weight: 800; font-size: 29px; margin-top: 1px; }
  .headline__sub { display: block; color: var(--white); font-weight: 600; font-size: 14px; margin-top: 3px; letter-spacing: .4px; }

  .badge-text { position: absolute; left: 56px; top: 288px; width: 134px; text-align: center; color: var(--white); font-family: var(--display-font); text-transform: uppercase; line-height: 1; }
  .badge-text__hours { display: block; font-size: 44px; font-weight: 600; }
  .badge-text__label { display: block; font-size: 19px; font-weight: 500; margin-top: 5px; line-height: 1.05; }

  /* contact block */
  .contact { position: absolute; left: 23px; top: 475px; color: var(--white); }
  .contact__row { display: flex; align-items: center; gap: 12px; font-size: 11px; font-weight: 500; height: 17px; }
  .contact__row--phone { font-size: 19px; font-weight: 800; height: 25px; gap: 8px; margin-bottom: 2px; }
  .contact__icon { width: 11px; height: 11px; flex: none; }
  .contact__row--phone .contact__icon { width: 14px; height: 14px; }

  /* back side */
  .services-title { position: absolute; left: 22px; top: 24px; width: 265px; height: 27px; background: var(--brand-blue); border-radius: 0 14px 14px 0; border-bottom: 2px solid var(--white); border-right: 2px solid var(--white); color: var(--white); font-weight: 700; font-size: 15.5px; line-height: 26px; padding-left: 14px; }
  .services { position: absolute; left: 26px; top: 66px; list-style: none; }
  .services__item { display: flex; align-items: flex-start; gap: 11px; color: var(--white); font-weight: 600; font-size: 14.4px; line-height: 18px; margin-bottom: 11px; }
  .services__icon { width: 22px; height: 22px; border-radius: 50%; flex: none; background: var(--brand-blue); border: 2px solid var(--soft-white); margin-top: -2px; position: relative; }
  .services__icon::after { content: ""; position: absolute; inset: 5px; border: 1.5px solid var(--white); border-radius: 2px; }

  .product { position: absolute; border-radius: 4px; }
  .product--split-ac { left: 243px; top: 112px; width: 122px; height: 44px; background: linear-gradient(180deg, #ffffff, #d8dde2); }
  .product--tank { left: 258px; top: 202px; width: 55px; height: 125px; background: linear-gradient(90deg, #d9dde1, #ffffff 45%, #cfd4d9); border-radius: 6px; }
  .product--outdoor { left: 307px; top: 281px; width: 57px; height: 52px; background: linear-gradient(180deg, #f2f4f6, #c9ced3); }
  .product--heater { left: 258px; top: 374px; width: 96px; height: 141px; background: linear-gradient(180deg, #ffffff, #e1e5e9); border-radius: 6px; }

  .voucher { position: absolute; left: 21px; top: 323px; width: 189px; height: 119px; border-radius: 14px; background: var(--white); border: 2px solid var(--brand-blue); overflow: hidden; font-family: var(--display-font); text-transform: uppercase; line-height: .95; }
  .voucher__value { position: absolute; left: 0; top: 0; width: 106px; height: 100%; background: var(--brand-blue); border-radius: 0 60px 60px 0; border-right: 3px solid var(--white); color: var(--white); text-align: center; padding-top: 8px; }
  .voucher__amount { display: block; font-size: 40px; font-weight: 600; }
  .voucher__amount sup { font-size: 18px; vertical-align: 16px; }
  .voucher__off { display: block; font-size: 40px; font-weight: 600; }
  .voucher__word { display: block; font-size: 17px; font-weight: 500; margin-top: 2px; }
  .voucher__limit { position: absolute; left: 113px; top: 14px; width: 70px; text-align: center; color: var(--brand-blue); font-family: var(--body-font); font-weight: 900; font-size: 18px; line-height: 1; }
  .voucher__limit span { display: block; }
  .voucher__per { font-family: var(--display-font); font-weight: 500; font-size: 26px; color: var(--bright-blue); }
  .voucher__limit .voucher__house { font-size: 15px; }
  .voucher__limit .voucher__hold { font-size: 19px; }
</style>
</head>
<body>

<!-- Front side -->
<section class="flyer flyer--front" aria-label="7Bram Plumbing flyer front">
  <svg class="flyer__shapes" viewBox="0 0 390 554">
    <defs>
      <linearGradient id="photoTone" x1="0" y1="0" x2="1" y2="1">
        <stop offset="0" stop-color="#e7ecf1"/>
        <stop offset=".45" stop-color="#2f5da0"/>
        <stop offset="1" stop-color="#1b3d73"/>
      </linearGradient>
    </defs>
    <path d="M292,0 C240,90 175,170 170,250 C165,330 203,402 255,428 C305,450 355,456 390,454 V0 Z" fill="none" stroke="var(--brand-blue)" stroke-width="10"/>
    <path role="img" aria-label="Photo of a plumber in blue overalls with a tool belt, plunger and tape" d="M300,0 C250,90 185,170 180,250 C175,330 210,398 260,422 C310,444 358,449 390,448 V0 Z" fill="url(#photoTone)"/>

    <g class="emergency-badge">
      <circle cx="123" cy="339" r="92" fill="var(--brand-blue)"/>
      <circle cx="123" cy="339" r="85" fill="var(--ring-grey)"/>
      <circle cx="123" cy="339" r="77" fill="var(--brand-blue)"/>
      <circle cx="123" cy="339" r="68" fill="var(--alert-red)" stroke="var(--white)" stroke-width="2"/>
    </g>

    <path d="M0,458 C90,443 190,446 262,470 C320,490 360,500 390,494 V554 H0 Z" fill="var(--brand-blue)"/>
    <path d="M205,458 C280,470 335,498 390,488" fill="none" stroke="var(--white)" stroke-width="3"/>
    <path d="M240,478 C300,494 345,506 390,500" fill="none" stroke="var(--bright-blue)" stroke-width="4"/>
  </svg>

  <div class="brand">
    <span class="brand__dot"></span>
    <span class="brand__name">7Bram Plumbing</span>
  </div>

  <h1 class="headline">
    <span class="headline__name">7Bram</span>
    <span class="headline__trade">Plumbing</span>
    <span class="headline__sub">&amp; Air-Conditiong</span>
  </h1>

  <p class="badge-text">
    <span class="badge-text__hours">24/7</span>
    <span class="badge-text__label">Emergency<br>Call Out</span>
  </p>

  <div class="contact">
    <p class="contact__row contact__row--phone">
      <svg class="contact__icon" viewBox="0 0 16 16"><circle cx="8" cy="8" r="8" fill="#fff"/><path d="M5 4 L6.6 4 L7.2 6 L6.2 6.8 C6.7 8 7.8 9.2 9.1 9.8 L9.9 8.8 L12 9.4 L12 11 C8 11.4 4.6 8 5 4 Z" fill="var(--brand-blue)"/></svg>
      0400 555 123
    </p>
    <p class="contact__row">
      <svg class="contact__icon" viewBox="0 0 16 16"><circle cx="8" cy="8" r="7" fill="none" stroke="#fff" stroke-width="1.5"/><ellipse cx="8" cy="8" rx="3" ry="7" fill="none" stroke="#fff" stroke-width="1.2"/><path d="M1 8 H15 M2.5 4.5 H13.5 M2.5 11.5 H13.5" stroke="#fff" stroke-width="1.2"/></svg>
      7bramplumbing.com
    </p>
    <p class="contact__row">
      <svg class="contact__icon" viewBox="0 0 16 16"><circle cx="8" cy="8" r="8" fill="#fff"/><rect x="4" y="5" width="8" height="6" fill="none" stroke="var(--brand-blue)" stroke-width="1.2"/><path d="M4 5 L8 8.5 L12 5" fill="none" stroke="var(--brand-blue)" stroke-width="1.2"/></svg>
      sam@7bramplumbing.com
    </p>
  </div>
</section>

<!-- Back side -->
<section class="flyer flyer--back" aria-label="7Bram Plumbing flyer back">
  <svg class="flyer__shapes" viewBox="0 0 390 554">
    <path d="M0,458 C90,443 190,446 262,470 C320,490 360,500 390,494 V554 H0 Z" fill="var(--brand-blue)"/>
    <path d="M205,458 C280,470 335,498 390,488" fill="none" stroke="var(--white)" stroke-width="3"/>
    <path d="M240,478 C300,494 345,506 390,500" fill="none" stroke="var(--bright-blue)" stroke-width="4"/>
  </svg>

  <h2 class="services-title">Aspects of plumbing we do</h2>

  <ul class="services">
    <li class="services__item"><span class="services__icon"></span>Hot water systems</li>
    <li class="services__item"><span class="services__icon"></span>Central Heating</li>
    <li class="services__item"><span class="services__icon"></span>Solar hot water<br>systems/ heat<br>pump systems</li>
    <li class="services__item"><span class="services__icon"></span>Gasfitting</li>
    <li class="services__item"><span class="services__icon"></span>Drainage</li>
    <li class="services__item"><span class="services__icon"></span>Roofing</li>
    <li class="services__item"><span class="services__icon"></span>Air-Conditioning</li>
  </ul>

  <div class="product product--split-ac" role="img" aria-label="Photo of a wall-mounted split air-conditioner"></div>
  <div class="product product--tank" role="img" aria-label="Photo of a heat pump hot water tank"></div>
  <div class="product product--outdoor" role="img" aria-label="Photo of an outdoor heat pump unit"></div>
  <div class="product product--heater" role="img" aria-label="Photo of a continuous flow gas hot water unit"></div>

  <div class="voucher">
    <p class="voucher__value">
      <span class="voucher__amount"><sup>$</sup>30</span>
      <span class="voucher__off">Off</span>
      <span class="voucher__word">Voucher</span>
    </p>
    <p class="voucher__limit">
      <span>Limit</span>
      <span class="voucher__per">1 Per</span>
      <span class="voucher__house">House</span>
      <span class="voucher__hold">Hold</span>
    </p>
  </div>

  <div class="contact">
    <p class="contact__row contact__row--phone">
      <svg class="contact__icon" viewBox="0 0 16 16"><circle cx="8" cy="8" r="8" fill="#fff"/><path d="M5 4 L6.6 4 L7.2 6 L6.2 6.8 C6.7 8 7.8 9.2 9.1 9.8 L9.9 8.8 L12 9.4 L12 11 C8 11.4 4.6 8 5 4 Z" fill="var(--brand-blue)"/></svg>
      0400 555 123
    </p>
    <p class="contact__row">
      <svg class="contact__icon" viewBox="0 0 16 16"><circle cx="8" cy="8" r="7" fill="none" stroke="#fff" stroke-width="1.5"/><ellipse cx="8" cy="8" rx="3" ry="7" fill="none" stroke="#fff" stroke-width="1.2"/><path d="M1 8 H15 M2.5 4.5 H13.5 M2.5 11.5 H13.5" stroke="#fff" stroke-width="1.2"/></svg>
      7bramplumbing.com
    </p>
    <p class="contact__row">
      <svg class="contact__icon" viewBox="0 0 16 16"><circle cx="8" cy="8" r="8" fill="#fff"/><rect x="4" y="5" width="8" height="6" fill="none" stroke="var(--brand-blue)" stroke-width="1.2"/><path d="M4 5 L8 8.5 L12 5" fill="none" stroke="var(--brand-blue)" stroke-width="1.2"/></svg>
      sam@7bramplumbing.com
    </p>
  </div>
</section>

</body>
</html>
```